Business Card Design Project

Business Card
We are rebranding with a new logo
Industry/Entity Type
Business
Contact Information for Business Card
Dennis Marlow +61 427581962 dennis@qovo.com.au P.O. Box 872 Kelvindale QLD 4309
Requirements
Must have
- Logo

```html
<!DOCTYPE html>
<html lang="en">
<head>
<meta charset="utf-8">
<title>Qovo International – Business Card</title>
<link rel="stylesheet" href="https://fonts.googleapis.com/css2?family=Jost:wght@400;500&display=swap">
<style>
  :root {
    --backdrop: #e4e5e7;
    --card: #f7f7f6;
    --ink: #2a2a2c;
    --brand-blue: #1a7fb8;
    --accent-orange: #e8731c;
  }
  html, body {
    margin: 0;
    padding: 0;
    width: 1200px;
    height: 1200px;
    overflow: hidden;
    background: var(--backdrop);
  }
  .canvas {
    width: 1200px;
    height: 1200px;
    display: flex;
    align-items: center;
    justify-content: center;
  }
  .business-card {
    position: relative;
    width: 1000px;
    height: 570px;
    background: var(--card);
    box-shadow: 0 2px 6px rgba(0,0,0,0.12);
    font-family: "Jost", sans-serif;
    color: var(--ink);
  }
  .brand {
    position: absolute;
    left: 95px;
    top: 225px;
    width: 345px;
    color: var(--brand-blue);
    font-weight: 500;
    text-align: center;
  }
  .brand-name {
    font-size: 92px;
    line-height: 1;
    letter-spacing: 6px;
  }
  .brand-tagline {
    margin-top: 14px;
    font-size: 29px;
    letter-spacing: 4.5px;
  }
  .contact {
    position: absolute;
    left: 530px;
    top: 188px;
  }
  .contact-name {
    font-size: 38px;
    font-weight: 400;
    letter-spacing: 3.5px;
    margin: 0 0 30px;
    line-height: 1;
  }
  .contact-list {
    list-style: none;
    margin: 0;
    padding: 0;
    font-size: 21px;
    letter-spacing: 2px;
    line-height: 34px;
  }
  .contact-item {
    display: flex;
    align-items: flex-start;
    margin-bottom: 22px;
  }
  .contact-icon {
    width: 22px;
    height: 22px;
    margin: 6px 22px 0 0;
    flex: none;
    fill: var(--accent-orange);
  }
</style>
</head>
<body>
<main class="canvas">
  <section class="business-card">
    <div class="brand">
      <div class="brand-name">QOVO</div>
      <div class="brand-tagline">INTERNATIONAL</div>
    </div>
    <div class="contact">
      <h1 class="contact-name">DENNIS MARLOW</h1>
      <ul class="contact-list">
        <li class="contact-item">
          <svg class="contact-icon" viewBox="0 0 24 24" aria-hidden="true"><path d="M9 3 L5 4.5 C3.5 9 6 17 12 21 L15.5 19 L13 15.5 L11 16.5 C9.3 14 8.5 11 8.8 8.5 L11 7.8 Z"/></svg>
          <span>+61 427581962</span>
        </li>
        <li class="contact-item">
          <svg class="contact-icon" viewBox="0 0 24 24" aria-hidden="true"><path d="M1 5 H23 V19 H1 Z M1 5 L12 13 L23 5" stroke="#f7f7f6" stroke-width="1.6"/></svg>
          <span>DENNIS@QOVO.COM.AU</span>
        </li>
        <li class="contact-item">
          <svg class="contact-icon" viewBox="0 0 24 24" aria-hidden="true"><path d="M12 1 C7.5 1 4.5 4.3 4.5 8.3 C4.5 13.5 12 23 12 23 C12 23 19.5 13.5 19.5 8.3 C19.5 4.3 16.5 1 12 1 Z M12 5.3 A3 3 0 1 1 12 11.3 A3 3 0 1 1 12 5.3 Z"/></svg>
          <span>P.O. BOX 872<br>KELVINDALE QLD 4309</span>
        </li>
      </ul>
    </div>
  </section>
</main>
</body>
</html>
```